Body therapist needs a business card

I need a card for my business which is teaching trainings in body therapy, the company is called Wexcombe Educational Group. I teach to massage therapists around Australia, South East Asia and the USA. I am attaching my logo which will guide you as to what colours I would like to have you consider. Please consult my website to find out more about what I do. www.corvantela.com.au

My name is Daniel Wexcombe. My phone number is (03) 9417 2608 or 0461753208. email is info@corvantela.com.au

```html
<!DOCTYPE html>
<html lang="en">
<head>
<meta charset="utf-8">
<title>Wexcombe Educational Group – Business Card</title>
<link href="https://fonts.googleapis.com/css2?family=Open+Sans:wght@400;600;700&display=swap" rel="stylesheet">
<style>
  :root {
    --page-bg: #e6e4e1;
    --brown: #7f4a22;
    --brown-dark: #5e3518;
    --crimson: #a3152a;
    --lime: #b4cc2c;
    --card-white: #f8f8f8;
    --ink-brown: #6b3a1c;
  }
  * { box-sizing: border-box; margin: 0; padding: 0; }
  html, body { width: 1200px; height: 1021px; overflow: hidden; }
  body {
    background: var(--page-bg);
    font-family: "Open Sans", Arial, sans-serif;
    position: relative;
  }
  .card {
    position: absolute;
    left: 300px;
    width: 600px;
    height: 343px;
    border-radius: 18px;
    overflow: hidden;
    box-shadow: 0 6px 18px rgba(0,0,0,0.18);
  }
  /* Front */
  .card-front { top: 110px; background: var(--brown); }
  .photo-circle {
    position: absolute;
    left: 300px;
    top: 30px;
    width: 330px;
    height: 330px;
    border-radius: 50%;
    background: radial-gradient(circle at 40% 40%, #8d5530 0%, #6a3c1d 70%, #5a3218 100%);
  }
  .front-name {
    position: absolute;
    left: 40px;
    top: 230px;
    color: #ffffff;
    font-size: 28px;
    font-weight: 400;
    line-height: 1.15;
    width: 260px;
  }
  /* Back */
  .card-back { top: 520px; background: linear-gradient(160deg, #ffffff 0%, var(--card-white) 55%, #e9e9e9 100%); }
  .brand {
    position: absolute;
    left: 40px;
    top: 140px;
    display: flex;
    align-items: center;
    gap: 14px;
  }
  .brand-dot {
    width: 44px; height: 44px;
    border-radius: 50%;
    background: var(--brown);
    flex: none;
  }
  .brand-name {
    color: var(--ink-brown);
    font-size: 21px;
    font-weight: 400;
    line-height: 1.2;
    width: 190px;
  }
  .divider {
    position: absolute;
    left: 300px;
    top: 95px;
    width: 2px;
    height: 150px;
    background: var(--lime);
  }
  .contact {
    position: absolute;
    left: 330px;
    top: 100px;
    color: var(--ink-brown);
  }
  .person-name { color: var(--crimson); font-size: 21px; font-weight: 700; }
  .person-role { font-size: 15px; margin-bottom: 14px; }
  .contact-list { list-style: none; font-size: 14.5px; line-height: 1.5; }
  .contact-list li { display: flex; align-items: center; gap: 8px; }
  .contact-list svg { width: 14px; height: 14px; flex: none; }
</style>
</head>
<body>

<section class="card card-front" aria-label="Card front">
  <div class="photo-circle" role="img" aria-label="Photo of a massage therapy session, toned in brown"></div>
  <p class="front-name">Wexcombe Educational Group</p>
</section>

<section class="card card-back" aria-label="Card back">
  <div class="brand">
    <span class="brand-dot"></span>
    <p class="brand-name">Wexcombe Educational Group</p>
  </div>
  <div class="divider"></div>
  <div class="contact">
    <p class="person-name">Daniel Wexcombe</p>
    <p class="person-role">Founder</p>
    <ul class="contact-list">
      <li>
        <svg viewBox="0 0 16 16" aria-hidden="true"><path fill="var(--crimson)" d="M3.6 1.5l2.3 2.3-1.3 1.9c.9 2 2.6 3.7 4.6 4.6l1.9-1.3 2.3 2.3-1.4 2.2C6.6 14.8 1.2 9.4 1.4 2.9z"/></svg>
        (03) 9417 2608
      </li>
      <li>
        <svg viewBox="0 0 16 16" aria-hidden="true"><rect x="4" y="1" width="8" height="14" rx="1.5" fill="none" stroke="var(--crimson)" stroke-width="1.6"/><circle cx="8" cy="12.5" r="0.9" fill="var(--crimson)"/></svg>
        0461753208
      </li>
      <li>
        <svg viewBox="0 0 16 16" aria-hidden="true"><rect x="1.5" y="3.5" width="13" height="9" fill="none" stroke="var(--crimson)" stroke-width="1.5"/><path d="M1.5 3.5L8 9l6.5-5.5" fill="none" stroke="var(--crimson)" stroke-width="1.5"/></svg>
        info@corvantela.com.au
      </li>
      <li>
        <svg viewBox="0 0 16 16" aria-hidden="true"><g fill="none" stroke="var(--crimson)" stroke-width="1.3"><circle cx="8" cy="8" r="6.3"/><ellipse cx="8" cy="8" rx="2.8" ry="6.3"/><path d="M1.7 8h12.6M2.8 4.7h10.4M2.8 11.3h10.4"/></g></svg>
        www.corvantela.com.au
      </li>
    </ul>
  </div>
</section>

</body>
</html>
```